Fahrzeugbeschriftung für Brandschutzservice
Zielgruppe
Siehe bitte www.lorventa.de
Aufgabenstellung
Brandschutzservice / Kundendienst / Feuerlöscher vor Ort beim Kunden prüfen /

```html
<!DOCTYPE html>
<html lang="de">
<head>
<meta charset="utf-8">
<title>Lorventa – Fahrzeugbeschriftung Heck</title>
<link href="https://fonts.googleapis.com/css2?family=Open+Sans:wght@400;600&display=swap" rel="stylesheet">
<style>
  :root {
    --page: #ffffff;
    --door: #e2e2e2;
    --fire-red: #e53a1f;
    --mascot-red: #d9262c;
    --ink: #111111;
    --band-black: #000000;
    --stripe-grey: #c9c9c9;
    --white: #ffffff;
  }
  html, body {
    margin: 0;
    width: 1200px;
    height: 866px;
    overflow: hidden;
    background: var(--page);
    font-family: "Open Sans", Arial, sans-serif;
  }
  .rear-wrap {
    position: absolute;
    left: 150px;
    top: 10px;
    width: 900px;
    height: 846px;
    overflow: hidden;
  }
  .rear-wrap svg.artwork {
    position: absolute;
    inset: 0;
  }
  .service-list {
    position: absolute;
    left: 463px;
    top: 44px;
    margin: 0;
    padding: 0;
    list-style: none;
    font-weight: 600;
    font-size: 50px;
    line-height: 50px;
    color: var(--ink);
    letter-spacing: 0.5px;
  }
  .company-address {
    position: absolute;
    right: 530px;
    top: 385px;
    margin: 0;
    font-style: normal;
    font-size: 24px;
    line-height: 31px;
    text-align: right;
    color: var(--ink);
    letter-spacing: 0.4px;
  }
  .contact-phone {
    position: absolute;
    left: 370px;
    top: 718px;
    width: 300px;
    text-align: center;
    font-size: 42px;
    line-height: 44px;
    color: var(--white);
    letter-spacing: 0.5px;
  }
  .contact-web {
    position: absolute;
    left: 0;
    right: 0;
    top: 748px;
    text-align: center;
    padding-left: 100px;
    font-weight: 600;
    font-size: 84px;
    line-height: 92px;
    color: var(--white);
  }
</style>
</head>
<body>
  <div class="rear-wrap">
    <svg class="artwork" width="900" height="846" viewBox="0 0 900 846">
      <defs>
        <linearGradient id="fireFade" x1="0" y1="1" x2="0" y2="0">
          <stop offset="0" stop-color="#e53a1f"/>
          <stop offset="0.6" stop-color="#e53a1f" stop-opacity="0.85"/>
          <stop offset="1" stop-color="#e53a1f" stop-opacity="0.15"/>
        </linearGradient>
        <radialGradient id="mascotTone" cx="0.55" cy="0.5" r="0.6">
          <stop offset="0" stop-color="#e8474c"/>
          <stop offset="1" stop-color="#c81f26"/>
        </radialGradient>
      </defs>

      <path class="door-panel" d="M0 0 H900 V583 Q450 700 0 590 Z" fill="var(--door)"/>

      <rect class="fire-area" x="0" y="98" width="430" height="266" fill="url(#fireFade)"
            role="img" aria-label="Illustration: rote Flammen, die von einem Wasserstrahl gelöscht werden"/>

      <rect class="mascot-area" x="470" y="215" width="400" height="360" rx="36" fill="url(#mascotTone)"
            role="img" aria-label="Illustration: fröhliche Feuerlöscher-Figur mit Schlauch, Daumen hoch"/>

      <path class="wave-black" d="M0 590 Q450 700 900 583 V846 H0 Z" fill="var(--band-black)"/>

      <path class="wave-stripe" d="M0 737 Q450 680 900 737 V846 H0 Z" fill="var(--stripe-grey)"/>
      <path class="wave-red" d="M0 747 Q450 692 900 747 V846 H0 Z" fill="var(--fire-red)"/>
    </svg>

    <ul class="service-list">
      <li>Beratung</li>
      <li>Verkauf</li>
      <li>Service</li>
    </ul>

    <address class="company-address">
      Lorventa GmbH<br>
      Lindenweg 12<br>
      07749 Talheim
    </address>

    <div class="contact-phone">03641 47219</div>
    <div class="contact-web">lorventa.de</div>
  </div>
</body>
</html>
```